Real estate company needs a letterhead design

A young real estate company needs a letterhead / stationery design, it should include the company's logo. It should look exactly the same as on the business cards. (With the phrase "a brand of KEV Wohnbau & Grundstücksentwicklung GmbH")

In addition, it should also include the 4 round seals.

color code blue # 00456b gray # 333333

Word and PDF are welcome.

KEV Wohnbau & Grundstücksentwicklung GmbH
Managing director: Mag. Lukas Fellnhuber
Matthias-Ortner-Strasse 3c / 41
6320 Angerfeld

Tel .: +436648172093
Email: office@wohnglanz-beispiel.at
Web: www.wohnglanz-beispiel.at

Sparkasse Almtal, Bergländer Sparkasse from 1882, Genossenschaftskasse
Anton-Weissauer-Strasse 7, 6320 Angerfeld
IBAN: AT31 4817 2964 0058 2316
BIC: GLMTAT44XXX
Account holder: KEV Wohnbau & Grundstücksentwicklung GmbH

FN: XXXXXXX
UID: XXXXXXX

```html
<!DOCTYPE html>
<html lang="en">
<head>
<meta charset="utf-8">
<title>Wohnglanz Letterhead</title>
<link href="https://fonts.googleapis.com/css2?family=Source+Sans+3:wght@400;600;700&display=swap" rel="stylesheet">
<style>
  :root {
    --brand-blue: #00456b;
    --brand-blue-dark: #002c45;
    --ink: #333333;
    --sidebar: #4d4d4d;
    --paper: #ffffff;
    --backdrop: #000000;
    --seal-red: #e2231a;
    --on-dark: #ffffff;
  }
  * { margin: 0; padding: 0; box-sizing: border-box; }
  html, body { width: 960px; height: 1200px; overflow: hidden; background: var(--backdrop); }
  body { font-family: "Source Sans 3", sans-serif; color: var(--ink); position: relative; }

  .letterhead { position: absolute; left: 76px; top: 77px; width: 808px; height: 1045px; background: var(--paper); }

  .brand { position: absolute; left: 42px; top: 60px; }
  .brand-name { font-size: 44px; font-weight: 700; color: var(--brand-blue); letter-spacing: 1.5px; line-height: 1; }
  .brand-tagline { font-size: 9px; font-weight: 600; color: var(--brand-blue); margin-top: 3px; white-space: nowrap; }

  .salutation { position: absolute; left: 42px; top: 263px; font-size: 15px; }
  .letter-body { position: absolute; left: 42px; top: 329px; width: 531px; font-size: 15px; line-height: 19px; text-align: justify; }
  .letter-body p { margin-bottom: 19px; }
  .letter-body p.lead { text-indent: 47px; }

  .sidebar { position: absolute; left: 604px; top: 0; width: 204px; height: 100%; background: var(--sidebar); color: var(--on-dark); }

  .director-tag { position: absolute; left: -19px; top: 45px; width: 204px; height: 40px; background: var(--brand-blue); padding: 6px 0 0 27px; font-size: 12.5px; line-height: 15px; }
  .director-tag strong { font-weight: 700; display: block; }
  .director-fold { position: absolute; left: -19px; top: 85px; }

  .contact-list { position: absolute; left: 18px; top: 111px; list-style: none; font-size: 12.5px; }
  .contact-list li { display: flex; align-items: center; height: 21.5px; white-space: nowrap; }
  .contact-list svg { margin-right: 7px; flex: none; }

  .address { position: absolute; left: 18px; top: 189px; font-size: 12.5px; line-height: 16px; }

  .seals { position: absolute; left: 11px; top: 305px; width: 180px; display: grid; grid-template-columns: 88px 88px; gap: 14px 7px; }

  .bank-list { position: absolute; left: 16px; top: 714px; list-style: none; font-size: 12.5px; }
  .bank-list li { height: 21.2px; display: flex; align-items: center; white-space: nowrap; }
  .bank-list li::before { content: ""; width: 6px; height: 6px; border-radius: 50%; background: var(--on-dark); margin-right: 4px; }

  .info-block { position: absolute; left: 16px; font-size: 12.5px; line-height: 16px; }
  .info-block strong { font-weight: 700; }
  .iban { top: 845px; }
  .holder { top: 911px; }
  .registry { top: 980px; }
</style>
</head>
<body>
  <main class="letterhead">
    <header class="brand">
      <div class="brand-name">WOHNGLANZ</div>
      <div class="brand-tagline">eine Marke der K E V Wohnbau &amp; Grundstücksentwicklung GmbH</div>
    </header>

    <p class="salutation">Dear Dr</p>

    <section class="letter-body">
      <p class="lead">Lorem ipsum dolor sit amet, consectetur adipiscing elit. Integer eu odio mattis, pulvinar turpis quis, faucibus nisl. Proin feugiat, erat vitae cursus pharetra, enim est semper ligula, in malesuada orci nisl et diam. Etiam elementum metus ac fringilla vulputate. Etiam mattis ligula sed ante mollis bibendum. Orci varius natoque penatibus et magnis dis parturient montes, nascetur ridiculus mus.</p>
      <p>Ut nibh augue, blandit ac orci ac, rutrum congue enim. Suspendisse gravida vulputate felis, quis interdum orci tincidunt quis. Praesent imperdiet maximus neque. Mauris ut dui enim. Nullam at efficitur elit. Donec ante ipsum, fermentum at lectus vel, blandit vulputate ante. Proin luctus suscipit diam id vestibulum. Morbi malesuada id mauris eget ullamcorper.</p>
      <p>Donec varius orci purus, vitae aliquam libero volutpat id. Integer sed imperdiet libero. Aliquam accumsan, risus sit amet ornare consectetur, turpis felis dictum justo, non rhoncus mauris dui sed velit. Pellentesque habitant morbi tristique senectus et netus et malesuada fames ac turpis egestas. Pellentesque tincidunt vitae ligula nec imperdiet. Donec sed congue enim. Nullam elementum faucibus nulla nec vestibulum. Sed at tempor ligula. In quis vulputate nunc. Integer et gravida lacus, ac tristique risus. Sed at vulputate nulla.</p>
      <p>Praesent blandit nunc eu efficitur commodo. In tempor nisi ex, vel venenatis ante vestibulum a. Duis vestibulum nibh a erat sagittis, nec euismod lorem varius. Nam ultricies turpis sed justo sollicitudin volutpat. Morbi sed mollis eros. Sed quis tortor id enim vehicula porttitor. Curabitur non aliquam ex. Phasellus dignissim fermentum elit, at finibus ligula mattis eget.</p>
    </section>

    <aside class="sidebar">
      <div class="director-tag"><strong>Mag. Lukas Fellnhuber</strong>Managing director:</div>
      <svg class="director-fold" width="19" height="8" viewBox="0 0 19 8"><polygon points="0,0 19,0 19,8" fill="var(--brand-blue-dark)"/></svg>

      <ul class="contact-list">
        <li>
          <svg width="16" height="16" viewBox="0 0 16 16"><rect width="16" height="16" rx="2" fill="#fff"/><path d="M5 3.5l2 2-1.2 1.4c.6 1.3 1.6 2.3 2.9 2.9L10 8.6l2 2-1.3 1.7C7 12 4 9 3.7 5z" fill="var(--brand-blue)"/></svg>
          +436648172093
        </li>
        <li>
          <svg width="16" height="16" viewBox="0 0 16 16"><rect width="16" height="16" rx="2" fill="#fff"/><rect x="3" y="4.5" width="10" height="7" fill="var(--brand-blue)"/><path d="M3 4.5l5 4 5-4" stroke="#fff" stroke-width="1" fill="none"/></svg>
          office@wohnglanz-beispiel.at
        </li>
        <li>
          <svg width="16" height="16" viewBox="0 0 16 16"><rect width="16" height="16" rx="2" fill="#fff"/><g fill="none" stroke="var(--brand-blue)" stroke-width="1.1"><circle cx="8" cy="8" r="5"/><ellipse cx="8" cy="8" rx="2.2" ry="5"/><path d="M3 8h10M4 5.5h8M4 10.5h8"/></g></svg>
          www.wohnglanz-beispiel.at
        </li>
      </ul>

      <p class="address">Matthias-Ortner-Strasse<br>3c / 41<br>6320 Angerfeld</p>

      <div class="seals">
        <svg role="img" aria-label="Certification seal" width="88" height="88" viewBox="0 0 88 88"><circle cx="44" cy="44" r="43" fill="#fff"/><circle cx="44" cy="44" r="41" fill="none" stroke="var(--seal-red)" stroke-width="2"/><circle cx="44" cy="44" r="24" fill="var(--seal-red)"/></svg>
        <svg role="img" aria-label="Certification seal" width="88" height="88" viewBox="0 0 88 88"><circle cx="44" cy="44" r="43" fill="#fff"/><circle cx="44" cy="44" r="41" fill="none" stroke="var(--seal-red)" stroke-width="2"/><circle cx="44" cy="44" r="24" fill="var(--seal-red)"/></svg>
        <svg role="img" aria-label="Certification seal" width="88" height="88" viewBox="0 0 88 88"><circle cx="44" cy="44" r="43" fill="#fff"/><circle cx="44" cy="44" r="41" fill="none" stroke="var(--seal-red)" stroke-width="2"/><circle cx="44" cy="44" r="24" fill="var(--seal-red)"/></svg>
        <svg role="img" aria-label="Certification seal" width="88" height="88" viewBox="0 0 88 88"><circle cx="44" cy="44" r="43" fill="#fff"/><circle cx="44" cy="44" r="41" fill="none" stroke="var(--seal-red)" stroke-width="2"/><circle cx="44" cy="44" r="24" fill="var(--seal-red)"/></svg>
      </div>

      <ul class="bank-list">
        <li>Sparkasse Almtal</li>
        <li>Bergländer Sparkasse from 1882</li>
        <li>Genossenschaftskasse</li>
        <li>Anton-Weissauer-Strasse 7</li>
        <li>6320 Angerfeld</li>
      </ul>

      <p class="info-block iban"><strong>IBAN:</strong><br>AT31 4817 2964 0058 2316<br>BIC: GLMTAT44XXX</p>
      <p class="info-block holder"><strong>Account holder:</strong><br>KEV Wohnbau &amp;<br>Grundstücksentwicklung GmbH</p>
      <p class="info-block registry"><strong>FN:</strong> XXXXXXX<br><strong>UID:</strong> XXXXXXX</p>
    </aside>
  </main>
</body>
</html>
```